Mobile Dental Clinic Signage

We have a company called Coastline mobile dental care.

We have 5 trucks and need the outsides of the truck designed.

Colours we like used is a sea blue, dark blue, light blue basically all the blue colours as well as grey and white. We do not like too simple but something bright and professional.

We will need the following put on the truck
- Mobile Dental Centre
- Our logo
- Contact number 1300TOOTHY
- website www.brelvo.net.au
- all social media symbols
- Somewhere on the truck have sections where is says
servicing aged care facilities, schools, corporations and aboriginal communities.

I have attached our current signage on the mobile clinic but we need this revamped. I have also attached a previous graphic designer work to give a idea although we where not that impressed with the designs

We like the swirf look but maybe in different colours. Hope all this makes sense. And if the design can cover the windows that would be great.

```html
<!DOCTYPE html>
<html lang="en">
<head>
<meta charset="utf-8">
<title>Mobile Dental Centre – Trailer Wrap</title>
<link rel="stylesheet" href="https://fonts.googleapis.com/css2?family=Lobster+Two:wght@700&family=Nunito:wght@600;700;800&display=swap">
<style>
  :root{
    --navy:#2b2671;
    --sea:#1f8fd6;
    --cyan:#3bb8ea;
    --sky:#e6f1f8;
    --mist:#cfe0ec;
    --grey:#eef0f2;
    --white:#ffffff;
  }
  *{box-sizing:border-box;margin:0;padding:0}
  html,body{width:1200px;height:1144px;overflow:hidden}
  body{background:var(--grey);font-family:"Nunito",sans-serif;position:relative}
  .wrap-side{position:absolute;left:40px;width:1120px;height:440px;overflow:hidden;
    background:linear-gradient(180deg,var(--white) 0%,var(--sky) 60%,var(--mist) 100%);
    border:2px solid #c3c9cf}
  .wrap-side--kerb{top:88px}
  .wrap-side--road{top:616px}
  .wrap-side svg.band{position:absolute;inset:0;width:1120px;height:440px}
  .wrap-side--road svg.band{transform:scaleX(-1)}
  .photo{position:absolute;top:0;height:440px;width:380px}
  .wrap-side--kerb .photo{left:0}
  .wrap-side--road .photo{right:0;transform:scaleX(-1)}
  .title{position:absolute;top:58px;font-family:"Lobster Two",cursive;font-weight:700;font-size:54px;line-height:1.1;color:var(--navy);letter-spacing:1px;white-space:nowrap}
  .pill{position:absolute;top:138px;background:var(--sea);color:var(--white);font-weight:800;font-size:24px;padding:3px 20px;border-radius:22px;white-space:nowrap}
  .services{position:absolute;top:192px;display:flex;gap:30px;font-weight:700;font-size:21px;color:var(--navy);line-height:1.25;white-space:nowrap}
  .services ul{list-style:none}
  .chev{color:var(--sea);font-weight:800}
  .logo-box{position:absolute;top:52px;width:180px;height:80px;background:var(--white);display:flex;align-items:center;gap:10px;padding:0 14px;box-shadow:0 1px 3px rgba(0,0,0,.15)}
  .logo-box .dot{flex:none;width:20px;height:20px;border-radius:50%;background:var(--navy)}
  .logo-box .name{font-weight:700;font-size:15px;line-height:1.15;color:var(--navy)}
  .social{position:absolute;top:158px;display:flex;align-items:center;gap:7px;font-weight:700;font-size:19px;color:var(--navy);white-space:nowrap}
  .social .sq{width:22px;height:22px;background:var(--navy);border-radius:3px}
  .contact{position:absolute;top:386px;display:flex;align-items:center;gap:28px;font-weight:700;font-size:24px;color:var(--white);white-space:nowrap}
  .contact span{display:flex;align-items:center;gap:8px}
  /* kerb side: photo left, text right */
  .wrap-side--kerb .title{left:420px}
  .wrap-side--kerb .pill{left:400px}
  .wrap-side--kerb .services{left:400px}
  .wrap-side--kerb .logo-box{right:30px}
  .wrap-side--kerb .social{right:30px}
  .wrap-side--kerb .contact{right:30px}
  /* road side: mirrored */
  .wrap-side--road .title{right:420px}
  .wrap-side--road .pill{right:400px}
  .wrap-side--road .services{right:400px;text-align:right}
  .wrap-side--road .logo-box{left:30px}
  .wrap-side--road .social{left:30px}
  .wrap-side--road .contact{left:30px}
</style>
</head>
<body>

<section class="wrap-side wrap-side--kerb">
  <svg class="photo" viewBox="0 0 400 440" preserveAspectRatio="none" role="img" aria-label="Photo of a smiling woman during a dental check-up with a dental mirror">
    <defs>
      <radialGradient id="photoTone" cx="0.55" cy="0.4" r="0.7">
        <stop offset="0" stop-color="#e9c4b5"/><stop offset="0.55" stop-color="#d9d6d8"/><stop offset="1" stop-color="#b9d3e6"/>
      </radialGradient>
    </defs>
    <path d="M0 0 H300 C390 60 400 250 350 340 L0 350 Z" fill="url(#photoTone)"/>
  </svg>
  <svg class="band" viewBox="0 0 1120 440" aria-hidden="true">
    <path d="M0 318 C320 268 720 300 1120 312 L1120 440 L0 440 Z" fill="var(--cyan)"/>
    <path d="M0 338 C320 296 720 322 1120 332 L1120 440 L0 440 Z" fill="var(--white)"/>
    <path d="M0 352 C320 316 720 338 1120 346 L1120 440 L0 440 Z" fill="var(--navy)"/>
  </svg>
  <h1 class="title">Mobile Dental Centre</h1>
  <div class="pill">SERVICING AGED CARE :</div>
  <div class="services">
    <ul><li><span class="chev">›</span> Facilities</li><li><span class="chev">›</span> Schools</li></ul>
    <ul><li><span class="chev">›</span> Corporations</li><li><span class="chev">›</span> Aboriginal Communities</li></ul>
  </div>
  <div class="logo-box"><span class="dot"></span><span class="name">Coastline mobile dental care</span></div>
  <div class="social">find us on <i class="sq"></i><i class="sq"></i><i class="sq"></i><i class="sq"></i><i class="sq"></i><i class="sq"></i></div>
  <div class="contact">
    <span><svg width="14" height="24" viewBox="0 0 14 24" aria-hidden="true"><rect x="1" y="1" width="12" height="22" rx="2" fill="none" stroke="#fff" stroke-width="2"/><circle cx="7" cy="19" r="1.5" fill="#fff"/></svg>(999) 555 0142</span>
    <span><svg width="22" height="22" viewBox="0 0 22 22" aria-hidden="true"><g fill="none" stroke="#fff" stroke-width="1.8"><circle cx="11" cy="11" r="9.5"/><ellipse cx="11" cy="11" rx="4" ry="9.5"/><path d="M1.5 11h19"/></g></svg>www.brelvo.net.au</span>
  </div>
</section>

<section class="wrap-side wrap-side--road">
  <svg class="photo" viewBox="0 0 400 440" preserveAspectRatio="none" role="img" aria-label="Photo of a smiling woman during a dental check-up with a dental mirror">
    <path d="M0 0 H300 C390 60 400 250 350 340 L0 350 Z" fill="url(#photoTone)"/>
  </svg>
  <svg class="band" viewBox="0 0 1120 440" aria-hidden="true">
    <path d="M0 318 C320 268 720 300 1120 312 L1120 440 L0 440 Z" fill="var(--cyan)"/>
    <path d="M0 338 C320 296 720 322 1120 332 L1120 440 L0 440 Z" fill="var(--white)"/>
    <path d="M0 352 C320 316 720 338 1120 346 L1120 440 L0 440 Z" fill="var(--navy)"/>
  </svg>
  <h1 class="title">Mobile Dental Centre</h1>
  <div class="pill">SERVICING AGED CARE :</div>
  <div class="services">
    <ul><li>Corporations <span class="chev">‹</span></li><li>Aboriginal Communities <span class="chev">‹</span></li></ul>
    <ul><li>Facilities <span class="chev">‹</span></li><li>Schools <span class="chev">‹</span></li></ul>
  </div>
  <div class="logo-box"><span class="dot"></span><span class="name">Coastline mobile dental care</span></div>
  <div class="social"><i class="sq"></i><i class="sq"></i><i class="sq"></i><i class="sq"></i><i class="sq"></i><i class="sq"></i> find us on</div>
  <div class="contact">
    <span>www.brelvo.net.au<svg width="22" height="22" viewBox="0 0 22 22" aria-hidden="true"><g fill="none" stroke="#fff" stroke-width="1.8"><circle cx="11" cy="11" r="9.5"/><ellipse cx="11" cy="11" rx="4" ry="9.5"/><path d="M1.5 11h19"/></g></svg></span>
    <span>(999) 555 0142<svg width="14" height="24" viewBox="0 0 14 24" aria-hidden="true"><rect x="1" y="1" width="12" height="22" rx="2" fill="none" stroke="#fff" stroke-width="2"/><circle cx="7" cy="19" r="1.5" fill="#fff"/></svg></span>
  </div>
</section>

</body>
</html>
```